Business Card Design

We require a Business card for a new business called Tallwood Coach Charter.
We offer Coach Charter/Transfers for sporting clubs, School groups, Elderly groups, business and for weddings around the ACT/NSW areas. Charters can be for a few hours,daily or out of town for several days or for groups coming into town and staying in the area.
We are a very small operation and would like our business card to have some colour and maybe something with a horizon and road travelled included. we are a company who likes to be helpful are friendly and have great customer service skills. we would like our card to represent our small but honest company. My partner has been in the Coach Industry for over 30 years and I myself for 10 years. Our coach is 57 seats and the colour is blue and silver.
Updates

To all designers

Thank you very much for your ideas and work put into a design for our business card
We hope to make a decision in the next few days, it is a tough decision as we really like a most of the designs put forward.
We hope to keep everyone updated a will let you know as soon as possible.

Thank you all again

We would just like to thank everyone for their Designs for our new Business card.

And to let you know we have finally made our choice.
Once again thank you and to let you know that this was a very hard decision and 
we would have liked to pick more than one.
Thanks to everyone again.

Target Market(s)

We have a very wide and varied customer field, would like to send business cards to the 120 Schools we have in our area at least.

Industry/Entity Type

Town

Contact Information for Business Card

Tallwood Coach Charter
Peter Maskell
24 Dunmore Place
Queanbeyan NSW 2620
ph: 0438192604
e-mail: peter.mk@mailvale.com

```html
<!DOCTYPE html>
<html lang="en">
<head>
<meta charset="utf-8">
<title>Tallwood Coach Charter – Business Card</title>
<link rel="stylesheet" href="https://fonts.googleapis.com/css2?family=Exo+2:wght@400;500&display=swap">
<style>
  :root {
    --page: #e9e9e7;
    --card: #f4f4f4;
    --card-edge: #ffffff;
    --brand-blue: #00aeef;
    --divider-grey: #8a8a8a;
    --ink: #222222;
    --icon-grey: #6d6d6d;
    --on-blue: #ffffff;
  }
  * { box-sizing: border-box; margin: 0; padding: 0; }
  html, body {
    width: 1200px; height: 899px; overflow: hidden;
    background: var(--page);
    font-family: "Exo 2", sans-serif;
  }
  .business-card {
    position: absolute; left: 60px; top: 140px;
    width: 1080px; height: 620px;
    background: radial-gradient(circle at 45% 40%, var(--card-edge), var(--card) 70%);
    box-shadow: 0 10px 30px rgba(0,0,0,.18);
    overflow: hidden;
  }
  .accent-panel { position: absolute; inset: 0; width: 1080px; height: 620px; }
  .brand-name {
    position: absolute; left: 92px; top: 150px;
    color: var(--brand-blue); font-weight: 500;
    text-transform: uppercase; line-height: 1.1;
  }
  .brand-name .primary { display: block; font-size: 60px; letter-spacing: 20px; }
  .brand-name .secondary { display: block; font-size: 24px; letter-spacing: 5px; margin-top: 4px; }
  .contact-block {
    position: absolute; left: 92px; top: 360px;
    color: var(--ink); font-size: 22px; line-height: 1.35;
  }
  .address { margin-bottom: 12px; font-size: 24px; }
  .contact-list { list-style: none; }
  .contact-list li { display: flex; align-items: center; gap: 14px; height: 34px; }
  .contact-list svg { width: 22px; height: 22px; fill: var(--icon-grey); flex: none; }
  .holder {
    position: absolute; right: 46px; top: 318px;
    color: var(--on-blue); text-align: right; text-transform: uppercase;
  }
  .holder-name { font-size: 32px; font-weight: 500; letter-spacing: 1px; }
  .holder-title { font-size: 22px; letter-spacing: 2px; }
</style>
</head>
<body>
  <main class="business-card">
    <svg class="accent-panel" viewBox="0 0 1080 620" aria-hidden="true">
      <path d="M812 0 Q668 300 850 620 L1080 620 L1080 0 Z" fill="var(--divider-grey)"/>
      <path d="M826 0 Q684 300 864 620 L1080 620 L1080 0 Z" fill="var(--brand-blue)"/>
    </svg>

    <h1 class="brand-name">
      <span class="primary">Tallwood</span>
      <span class="secondary">Coach Charter</span>
    </h1>

    <section class="contact-block">
      <p class="address">24 Dunmore Place<br>Queanbeyan NSW 2620</p>
      <ul class="contact-list">
        <li><svg viewBox="0 0 24 24"><path d="M6.6 10.8a15 15 0 0 0 6.6 6.6l2.2-2.2a1 1 0 0 1 1-.25 11.4 11.4 0 0 0 3.6.57 1 1 0 0 1 1 1V20a1 1 0 0 1-1 1A17 17 0 0 1 3 4a1 1 0 0 1 1-1h3.5a1 1 0 0 1 1 1c0 1.25.2 2.45.57 3.6a1 1 0 0 1-.25 1z"/></svg>0438 192 604</li>
        <li><svg viewBox="0 0 24 24"><path d="M7 1h10a2 2 0 0 1 2 2v18a2 2 0 0 1-2 2H7a2 2 0 0 1-2-2V3a2 2 0 0 1 2-2zm0 3v14h10V4zm5 15.5a1 1 0 1 0 0 2 1 1 0 0 0 0-2z"/></svg>0438 192 604</li>
        <li><svg viewBox="0 0 24 24"><path d="M7 2h8l3 3v5h2a2 2 0 0 1 2 2v9H2v-9a2 2 0 0 1 2-2h3zm2 2v6h7V6h-2V4zM5 14v2h3v-2zm5 0v2h3v-2zm5 0v2h3v-2z"/></svg>0438 192 604</li>
        <li><svg viewBox="0 0 24 24"><path d="M2 5h20v14H2zm2 2v.5l8 5.5 8-5.5V7zm0 2.9V17h16V9.9l-8 5.5z"/></svg>peter.mk@mailvale.com</li>
        <li><svg viewBox="0 0 24 24"><path d="M12 2a10 10 0 1 0 0 20 10 10 0 0 0 0-20zm6.9 9h-3a15 15 0 0 0-1.4-6.1A8 8 0 0 1 18.9 11zM12 4.1c.9 1.2 1.8 3.6 1.9 6.9h-3.8c.1-3.3 1-5.7 1.9-6.9zM9.5 4.9A15 15 0 0 0 8.1 11h-3a8 8 0 0 1 4.4-6.1zM5.1 13h3a15 15 0 0 0 1.4 6.1A8 8 0 0 1 5.1 13zm6.9 6.9c-.9-1.2-1.8-3.6-1.9-6.9h3.8c-.1 3.3-1 5.7-1.9 6.9zm2.5-.8a15 15 0 0 0 1.4-6.1h3a8 8 0 0 1-4.4 6.1z"/></svg>www.tallwoodcoaches.com.au</li>
      </ul>
    </section>

    <section class="holder">
      <p class="holder-name">Peter Maskell</p>
      <p class="holder-title">Financial Advisor</p>
    </section>
  </main>
</body>
</html>
```